Business card and stationary for Intellectual Property Consultant & Law Firm
Harborline Claims Omniworks
Business card and stationary for Intellectual Property Consultant & Law Firm - Law
Creative Brief
Simple
Dorin Makalesu
President Director
Kelor Business Center 11th Floor Jl. Raya Wibisana Kav.37-38 Jakarta Pusat 10485, Indonesia
office@harborlineclaims.example
www.harborlineclaims.example
Member: OQRU, EKLM, UVBO, WDGF
Please add Intellectual Property Rights Consultant & Law Firm for letterhead additional of our email : hbl42@harborlineclaims.example; marks@harborlineclaims.example
please add Branch office : Surabaya (+6231) 480 3926 Medan (+6261) 819 4057 Solo (+62271) 634 918
trelvorin trelvorin
Dear All, Please provide me the stationary : letterhead, envelope, cds, ballpoint, ruler, stamps, usb sticks etc
dunmoral dunmoral
Please upload Ai or eps file of your logo thankyou
Please add : Intellectual Property Rights Consultant & Law Firm in envelope and letter head.

```html
<!DOCTYPE html>
<html lang="en">
<head>
<meta charset="utf-8">
<title>Harborline Claims Omniworks – Business Card</title>
<link href="https://fonts.googleapis.com/css2?family=Quicksand:wght@500;600;700&family=Exo+2:wght@400;600&display=swap" rel="stylesheet">
<style>
  :root{
    --backdrop:#d6d6d6;
    --card-white:#ffffff;
    --slate:#6b6c6f;
    --slate-dark:#58595c;
    --ink:#4a4b4e;
    --gold:#e9a321;
    --gold-light:#f6c24a;
    --accent:#1fa3c4;
    --on-slate:#ffffff;
  }
  *{margin:0;padding:0;box-sizing:border-box}
  html,body{width:1200px;height:818px;overflow:hidden}
  body{background:var(--backdrop);font-family:"Exo 2",sans-serif;position:relative}

  .card{position:absolute;top:259px;width:520px;height:300px;border-radius:16px;overflow:hidden;background:var(--card-white)}
  .card--front{left:50px}
  .card--back{left:630px}

  .brand{display:flex;align-items:center;gap:10px;font-family:"Quicksand",sans-serif;font-weight:700;color:var(--ink);line-height:1.05}
  .brand__mark{width:16px;height:16px;background:var(--accent);flex:none}
  .card--front .brand{position:absolute;left:0;right:0;top:0;bottom:0;justify-content:center;font-size:24px}
  .brand__name{display:block;max-width:220px}
  .card--back .brand{position:absolute;left:34px;top:26px;font-size:17px}
  .card--back .brand__name{max-width:160px}

  .card__art{position:absolute;inset:0}

  .holder{position:absolute;left:34px;top:196px;color:var(--on-slate)}
  .holder__name{font-size:17px;font-weight:600;letter-spacing:1.5px}
  .holder__title{font-size:8.5px;letter-spacing:1.8px;margin-top:3px;opacity:.9}

  .contact{position:absolute;right:26px;top:150px;text-align:right;color:var(--on-slate);font-size:8.5px;line-height:1.45}
  .contact__address{margin-bottom:10px}
  .contact__row{display:flex;justify-content:flex-end;align-items:center;gap:6px}
  .contact__icon{width:8px;height:8px;flex:none}
</style>
</head>
<body>

<section class="card card--front" aria-label="Card front">
  <div class="brand">
    <span class="brand__mark"></span>
    <span class="brand__name">Harborline Claims Omniworks</span>
  </div>
</section>

<section class="card card--back" aria-label="Card back">
  <svg class="card__art" width="520" height="300" viewBox="0 0 520 300" aria-hidden="true">
    <defs>
      <linearGradient id="goldSweep" x1="0" x2="1" y1="0" y2="0">
        <stop offset="0" stop-color="var(--gold)"/>
        <stop offset=".5" stop-color="var(--gold-light)"/>
        <stop offset="1" stop-color="var(--gold)"/>
      </linearGradient>
    </defs>
    <path d="M0,168 C150,130 300,198 520,112 L520,300 L0,300 Z" fill="var(--slate)"/>
    <g fill="none" stroke="url(#goldSweep)" stroke-linecap="round">
      <path d="M0,150 C160,112 300,178 520,92" stroke-width="7"/>
      <path d="M60,148 C200,120 320,170 520,100" stroke-width="4"/>
      <path d="M140,152 C260,132 360,162 520,108" stroke-width="3"/>
      <path d="M230,160 C320,150 420,150 520,120" stroke-width="2"/>
    </g>
  </svg>

  <div class="brand">
    <span class="brand__mark"></span>
    <span class="brand__name">Harborline Claims Omniworks</span>
  </div>

  <div class="holder">
    <div class="holder__name">RAVEL OTSEN</div>
    <div class="holder__title">MANAGING DIRECTOR</div>
  </div>

  <div class="contact">
    <div class="contact__address">Kelor Business Center 11th Floor<br>Jakarta Pusat 10485</div>
    <div class="contact__row">(+6231) 480 3926
      <svg class="contact__icon" viewBox="0 0 10 10"><path d="M2,1 L4,1 L4.6,3 L3.4,4 C4,5.4 4.8,6.2 6,6.8 L7,5.6 L9,6.2 L9,8.2 C5,8.6 1.4,5 2,1 Z" fill="var(--on-slate)"/></svg></div>
    <div class="contact__row">(+6261) 819 4057
      <svg class="contact__icon" viewBox="0 0 10 10"><path d="M2,1 L4,1 L4.6,3 L3.4,4 C4,5.4 4.8,6.2 6,6.8 L7,5.6 L9,6.2 L9,8.2 C5,8.6 1.4,5 2,1 Z" fill="var(--on-slate)"/></svg></div>
    <div class="contact__row">(+62271) 634 918
      <svg class="contact__icon" viewBox="0 0 10 10"><path d="M2,1 L4,1 L4.6,3 L3.4,4 C4,5.4 4.8,6.2 6,6.8 L7,5.6 L9,6.2 L9,8.2 C5,8.6 1.4,5 2,1 Z" fill="var(--on-slate)"/></svg></div>
    <div class="contact__row">office@harborlineclaims.example
      <svg class="contact__icon" viewBox="0 0 10 10"><rect x="1" y="2.5" width="8" height="5.5" fill="none" stroke="var(--on-slate)"/><path d="M1,2.5 L5,5.5 L9,2.5" fill="none" stroke="var(--on-slate)"/></svg></div>
    <div class="contact__row">www.harborlineclaims.example
      <svg class="contact__icon" viewBox="0 0 10 10"><circle cx="5" cy="5" r="4" fill="none" stroke="var(--on-slate)"/><path d="M1,5 H9 M5,1 C3,3.5 3,6.5 5,9 C7,6.5 7,3.5 5,1" fill="none" stroke="var(--on-slate)" stroke-width=".8"/></svg></div>
  </div>
</section>

</body>
</html>
```